Presentation Folder for dental clinic

We need a presentation folder design. The presentation folder is what we give to our patients with treatment plans, quotes, images, information sheets etc.
I have uploaded current stationary designs for assistance as well as a photo of our external sign design.
We are an upmarket dental clinic.
Professionalism and customer service is key to us.
We provide information in presentation folders to give to patients.
It needs to memorable and a statement to who we are.

Target Market(s)

Main patient base is Male and Female 40 years old to 70 years old

Industry/Entity Type

Dental Clinic

Font styles to use
Serif
Sans Serif

Requirements
Must have
• Design:
• -Professional
• -Timeless
• -Modern
• - Memorable
• - Statement (if a patient puts down the folder, it will be easily identifiable with as Morvel Dentals folder)
• Logo
• Address, phone, email, website
• Dr Leon Brisco name and degree details
• Colour scheme to match current logos and branding
• "Your Smile Our Passion" quote
Nice to have
• Services listed:
• - Sleep Dentistry
• - Happy Gas
• - Dental Implants
• - Cosmetic Dentistry
• - Oral Surgery
• - Clearotune
• - Teeth Whitening
• - General Dentistry
• - Childrens Dentistry
• See website www.morveldental.com.au
Should not have
• Dental cliche photos

```html
<!DOCTYPE html>
<html lang="en">
<head>
<meta charset="utf-8">
<title>Morvel Dentals – Presentation Folder</title>
<link href="https://fonts.googleapis.com/css2?family=Roboto:wght@400;500;700&display=swap" rel="stylesheet">
<style>
  :root {
    --purple: #7f4597;
    --purple-light: #b07ccb;
    --grey: #9a9b9e;
    --charcoal: #3a3a3c;
    --white: #ffffff;
    --stage: #e4e4e4;
  }
  * { margin: 0; padding: 0; box-sizing: border-box; }
  html, body { width: 1200px; height: 1200px; overflow: hidden; }
  body {
    background: var(--stage);
    font-family: "Roboto", Arial, sans-serif;
    position: relative;
  }
  .folder-spread {
    position: absolute;
    left: 50px; top: 210px;
    width: 1100px; height: 780px;
    display: flex;
    box-shadow: 0 12px 30px rgba(0,0,0,0.18);
  }
  .panel { position: relative; width: 550px; height: 780px; overflow: hidden; }

  /* Back cover */
  .back-cover { background: var(--purple); color: var(--white); }
  .back-cover .corner-shapes { position: absolute; left: 0; top: 0; }
  .services-list { list-style: none; position: absolute; left: 0; top: 0; }
  .services-list li {
    position: absolute;
    font-size: 11px; font-weight: 700;
    white-space: nowrap; color: var(--white);
  }
  .passion-block {
    position: absolute; left: 55px; top: 318px; width: 440px;
    text-align: center;
  }
  .service-icons { display: flex; justify-content: center; gap: 14px; margin-bottom: 14px; }
  .service-icons svg { width: 64px; height: 64px; }
  .tagline { font-size: 30px; font-weight: 500; letter-spacing: 0.5px; margin-bottom: 10px; }
  .tagline-copy { font-size: 11px; line-height: 1.45; font-weight: 400; }
  .back-contact {
    position: absolute; left: 0; width: 550px; top: 640px;
    text-align: center; font-weight: 700;
  }
  .back-contact .phone { font-size: 24px; letter-spacing: 0.5px; }
  .back-contact .web { font-size: 15px; }

  /* Front cover */
  .front-cover { background: var(--white); }
  .brand-name {
    position: absolute; left: 0; width: 550px; top: 258px;
    text-align: center; font-size: 54px; font-weight: 500;
    color: var(--purple); letter-spacing: -0.5px;
  }
  .contact-band { position: absolute; left: 0; bottom: 0; width: 550px; height: 72px; }
  .contact-band svg { position: absolute; left: 0; top: 0; }
  .practitioner {
    position: absolute; right: 356px; top: 11px;
    text-align: right; color: var(--white);
  }
  .practitioner .name { font-size: 12px; font-weight: 700; margin-bottom: 3px; white-space: nowrap; }
  .practitioner .credential { font-size: 6.5px; font-weight: 500; line-height: 1.3; white-space: nowrap; }
  .band-details {
    position: absolute; top: 22px;
    font-size: 8.5px; line-height: 1.7; color: var(--white); white-space: nowrap;
  }
  .band-details.address { left: 240px; }
  .band-details.online { right: 12px; text-align: right; }
  .band-details .label { color: var(--purple-light); margin-right: 4px; }
</style>
</head>
<body>
<main class="folder-spread">

  <section class="panel back-cover">
    <svg class="corner-shapes" width="550" height="780" viewBox="0 0 550 780">
      <polygon points="222,0 550,0 550,300" fill="var(--white)"/>
      <polygon points="236,0 550,0 550,286" fill="var(--grey)"/>
    </svg>
    <ul class="services-list">
      <li style="top:16px; left:268px;">Sleep Dentistry</li>
      <li style="top:32px; left:286px;">Happy Gas</li>
      <li style="top:48px; left:304px;">Dental Implants</li>
      <li style="top:64px; left:322px;">Cosmetic Dentistry</li>
      <li style="top:80px; left:340px;">Oral Surgery</li>
      <li style="top:96px; left:358px;">Clearotune</li>
      <li style="top:112px; left:376px;">Teeth Whitening</li>
      <li style="top:128px; left:394px;">General Dentistry</li>
      <li style="top:144px; left:412px;">Childrens Dentistry</li>
    </ul>

    <div class="passion-block">
      <div class="service-icons">
        <svg viewBox="0 0 64 64" aria-label="Sleep dentistry">
          <circle cx="32" cy="32" r="32" fill="var(--white)"/>
          <path d="M16 36 L30 40 L44 32 M22 38 L22 46 M36 37 L36 46 M20 46 L40 46" fill="none" stroke="var(--purple)" stroke-width="2.2" stroke-linecap="round"/>
          <circle cx="20" cy="31" r="3" fill="none" stroke="var(--purple)" stroke-width="2"/>
          <text x="30" y="26" font-size="10" font-weight="700" fill="var(--purple)">z<tspan font-size="8" dy="-4">z</tspan><tspan font-size="6" dy="-3">z</tspan></text>
        </svg>
        <svg viewBox="0 0 64 64" aria-label="Dental implants">
          <circle cx="32" cy="32" r="32" fill="var(--white)"/>
          <path d="M22 18 Q32 12 42 18 Q44 26 40 28 L24 28 Q20 26 22 18 Z" fill="none" stroke="var(--purple)" stroke-width="2.2"/>
          <path d="M26 32 L38 32 M27 36 L37 36 M28 40 L36 40 M29 44 L35 44 M32 44 L32 50" stroke="var(--purple)" stroke-width="2.2" stroke-linecap="round"/>
        </svg>
        <svg viewBox="0 0 64 64" aria-label="Teeth whitening">
          <circle cx="32" cy="32" r="32" fill="var(--white)"/>
          <path d="M22 24 Q26 18 32 22 Q38 18 42 24 Q44 32 40 38 L38 46 Q35 48 34 42 L32 36 L30 42 Q29 48 26 46 L24 38 Q20 32 22 24 Z" fill="none" stroke="var(--purple)" stroke-width="2.2" stroke-linejoin="round"/>
          <path d="M32 10 L32 14 M18 16 L21 19 M46 16 L43 19 M12 28 L16 28 M52 28 L48 28" stroke="var(--purple)" stroke-width="2" stroke-linecap="round"/>
        </svg>
      </div>
      <h2 class="tagline">Your Smile. Our Passion.</h2>
      <p class="tagline-copy">Our goal is help you show off your smile, eat any type of food without fear, and talk confidently. Dr. Leon has relentless pushed excellence in all aspects of dentistry. Leon loves helping people. He will always, “Do unto others as you would have others do unto you.”</p>
    </div>

    <div class="back-contact">
      <div class="phone">03 9000 4187</div>
      <div class="web">morveldental.com.au</div>
    </div>
  </section>

  <section class="panel front-cover">
    <h1 class="brand-name">Morvel Dental</h1>

    <div class="contact-band">
      <svg width="550" height="72" viewBox="0 0 550 72">
        <polygon points="0,0 205,0 228,72 0,72" fill="var(--purple)"/>
        <polygon points="214,0 550,0 550,72 237,72" fill="var(--charcoal)"/>
      </svg>
      <div class="practitioner">
        <div class="name">Dr. Leon Brisco &amp; Associates</div>
        <div class="credential">B.D.S Ashford College London</div>
        <div class="credential">Graduate Diploma in Clinical Dentistry</div>
        <div class="credential">(IV Sedation &amp; Pain Control) Carrow University</div>
      </div>
      <div class="band-details address">
        <div>214 Kessel Road, Brightvale Vic 3190</div>
        <div><span class="label">e-mail</span>info@morveldental.com.au</div>
      </div>
      <div class="band-details online">
        <div><span class="label">phone</span>03 9000 4187</div>
        <div><span class="label">website</span>morveldental.com.au</div>
      </div>
    </div>
  </section>

</main>
</body>
</html>
```